Postcard for Online Training Company for Real Estate Agents

We need a high-end professionally designed 2 sided color postcard to send out to Real Estate Agents to use our online, on-demand training service. We would like it to look clean and not busy. Our color scheme is Turquoise, Black and Blue. Color scheme can be seen on website address. Our main target audience are people who just entered the real estate profession. Most of them do no get an on-boarding training if they are not with a big company. We provide very low cost, highly professional training. For just $24.99 per month they have access to all the on-demand training of how to be a real estate agent. The real estate exam to get a license only has the laws and not how to be a a real estate agent.

This will also be use for small companies who do have their own training program for new real estate agent employees.

Target Market(s)

New Real Estate Agents

Industry/Entity Type

Real Estate Agent

Font styles to use
Serif
Sans Serif

Colors
33b8a4
0455a3
000000
b2b2b2

Requirements
Must have
• Both Sides Design Requirements:
• Includes Website address
• Includes Logo
• Includes Price of $24.99 per month (in some shape)
• Front needs to have these two sentences:
• “We help Real Estate agents learn how to close more business and make money”
• “On-Boarding for new agents”
• Back needs to have these 4 questions:
• "Just passed the Real Estate exam?"
• “How do I find clients?”
• “What are the steps to selling a home?”
• “How do I open escrow?”
• Website Address:
• BrightlaneSkillhouse.com
• Logo:
• Attached
Should not have
• This should not look like it is trying to sell a house or look like it is from real estate agent

```html
<!DOCTYPE html>
<html lang="en">
<head>
<meta charset="utf-8">
<title>Brightlane Skillhouse Postcard</title>
<link rel="stylesheet" href="https://fonts.googleapis.com/css2?family=Quicksand:wght@500;600;700&display=swap">
<style>
  :root {
    --turquoise: #17a3bf;
    --charcoal: #444547;
    --charcoal-dark: #333436;
    --paper: #ffffff;
    --mist: #eef0f1;
    --stamp: #c2c2c2;
    --stage: #e4e4e4;
    --ink: #333333;
  }
  html, body {
    margin: 0;
    padding: 0;
    width: 1200px;
    height: 1200px;
    overflow: hidden;
    background: var(--stage);
    font-family: "Quicksand", sans-serif;
  }
  .postcard {
    position: absolute;
    left: 257px;
    width: 660px;
    height: 512px;
    box-shadow: 0 3px 8px rgba(0,0,0,0.25);
    background: var(--paper);
  }
  .postcard--front { top: 56px; }
  .postcard--back { top: 623px; }
  .postcard svg { display: block; width: 100%; height: 100%; }
  .photo-ring { fill: none; stroke: var(--turquoise); stroke-width: 9; }
  .headline { font-family: "Quicksand", sans-serif; font-weight: 700; }
  .copy { font-family: "Quicksand", sans-serif; font-weight: 600; }
</style>
</head>
<body>

<section class="postcard postcard--front" aria-label="Postcard front">
  <svg viewBox="0 0 770 597" xmlns="http://www.w3.org/2000/svg">
    <defs>
      <linearGradient id="front-dark" x1="0" y1="0" x2="1" y2="1">
        <stop offset="0" stop-color="#3d3e40"/>
        <stop offset="1" stop-color="#5a5b5d"/>
      </linearGradient>
      <linearGradient id="couple-tone" x1="0" y1="0" x2="1" y2="1">
        <stop offset="0" stop-color="#eef3f6"/>
        <stop offset="0.55" stop-color="#bfdbe6"/>
        <stop offset="1" stop-color="#c9a58a"/>
      </linearGradient>
      <linearGradient id="mist" x1="0" y1="0" x2="0" y2="1">
        <stop offset="0" stop-color="#f4f5f6"/>
        <stop offset="1" stop-color="#e6e8ea"/>
      </linearGradient>
      <clipPath id="f-c1"><circle cx="270" cy="280" r="72"/></clipPath>
      <clipPath id="f-c2"><circle cx="455" cy="310" r="78"/></clipPath>
      <clipPath id="f-c3"><circle cx="650" cy="335" r="82"/></clipPath>
    </defs>

    <rect class="card-base" width="770" height="597" fill="url(#mist)"/>
    <polygon class="dark-panel" points="495,0 770,0 770,395 300,290" fill="url(#front-dark)"/>
    <rect role="img" aria-label="Photo of a smiling young couple holding up new house keys" x="0" y="0" width="0" height="0"/>
    <polygon role="img" aria-label="Photo of a smiling young couple holding up new house keys" points="0,0 470,0 120,395 0,330" fill="url(#couple-tone)"/>
    <polyline class="accent-stroke" points="0,330 120,395 480,0" fill="none" stroke="var(--turquoise)" stroke-width="10"/>
    <polygon class="accent-band" points="460,0 498,0 170,362 150,380" fill="var(--turquoise)"/>
    <polygon class="accent-band" points="300,290 770,390 770,405 300,300" fill="var(--turquoise)"/>

    <g class="photo-circle">
      <circle cx="270" cy="280" r="72" fill="#d9dfe3" role="img" aria-label="Photo of a training meeting at a table"/>
      <circle class="photo-ring" cx="270" cy="280" r="76"/>
    </g>
    <g class="photo-circle">
      <circle cx="455" cy="310" r="78" fill="#c8c0b4" role="img" aria-label="Photo of a woman reading documents at home"/>
      <circle class="photo-ring" cx="455" cy="310" r="82"/>
    </g>
    <g class="photo-circle">
      <circle cx="650" cy="335" r="82" fill="#9fb58a" role="img" aria-label="Photo of a father and son by a sale sign"/>
      <circle class="photo-ring" cx="650" cy="335" r="86"/>
    </g>

    <g class="tagline" text-anchor="end">
      <text class="headline" x="722" y="105" font-size="48" fill="var(--turquoise)">We help</text>
      <text class="copy" x="722" y="130" font-size="21" fill="#ffffff">Real Estate agents learn</text>
      <text class="copy" x="722" y="159" font-size="21" fill="var(--turquoise)">how to close more business</text>
      <text class="headline" x="722" y="192" font-size="30" fill="#ffffff">&amp; make money</text>
    </g>

    <text class="headline" x="62" y="458" font-size="28" fill="var(--ink)">On-Boarding <tspan fill="var(--turquoise)">for new agents</tspan></text>

    <rect class="contact-pill" x="52" y="482" width="406" height="43" rx="21.5" fill="var(--turquoise)"/>
    <text class="headline" x="255" y="511" font-size="22" fill="#ffffff" text-anchor="middle">Contact us at: 415.555.0142</text>

    <text class="brand-name headline" x="606" y="510" font-size="22" fill="var(--turquoise)" text-anchor="middle">BrightlaneSkillhouse</text>

    <polygon class="footer-band" points="0,552 770,540 770,597 0,597" fill="var(--turquoise)"/>
    <polygon class="footer-strip" points="0,580 770,553 770,597 0,597" fill="var(--charcoal)"/>
  </svg>
</section>

<section class="postcard postcard--back" aria-label="Postcard back">
  <svg viewBox="0 0 770 597" xmlns="http://www.w3.org/2000/svg">
    <defs>
      <linearGradient id="back-dark" x1="0" y1="0" x2="1" y2="1">
        <stop offset="0" stop-color="#3e3f41"/>
        <stop offset="1" stop-color="#525355"/>
      </linearGradient>
    </defs>

    <rect width="770" height="597" fill="var(--paper)"/>
    <polygon class="dark-panel" points="0,150 300,45 478,575 0,575" fill="url(#back-dark)"/>
    <polyline class="accent-stroke" points="300,45 480,575" fill="none" stroke="var(--turquoise)" stroke-width="5"/>
    <polygon class="price-panel" points="0,0 330,0 125,232 0,170" fill="var(--turquoise)"/>
    <polyline points="0,170 125,232 330,0" fill="none" stroke="#ffffff" stroke-width="5"/>

    <rect class="stamp-box" x="657" y="44" width="74" height="74" fill="var(--stamp)"/>

    <g class="price" fill="#ffffff">
      <text class="headline" x="46" y="70" font-size="48">Price</text>
      <text class="headline" x="46" y="110" font-size="36">$24.99</text>
      <text class="headline" x="46" y="142" font-size="24">per month</text>
    </g>

    <g class="photo-circle">
      <circle cx="352" cy="185" r="78" fill="#dfe6ec" role="img" aria-label="Photo of a small model house on a desk"/>
      <circle class="photo-ring" cx="352" cy="185" r="82"/>
    </g>
    <g class="photo-circle">
      <circle cx="432" cy="380" r="86" fill="#b8614f" role="img" aria-label="Photo of a happy couple in front of a sold sign"/>
      <circle class="photo-ring" cx="432" cy="380" r="90"/>
    </g>

    <g class="questions copy" font-size="19" fill="#ffffff">
      <circle cx="56" cy="298" r="6" fill="var(--turquoise)"/>
      <text x="80" y="305">Just passed the</text>
      <text x="80" y="329">Real Estate exam?</text>
      <circle cx="56" cy="351" r="6" fill="var(--turquoise)"/>
      <text x="80" y="358">How do I find clients?</text>
      <circle cx="56" cy="380" r="6" fill="var(--turquoise)"/>
      <text x="80" y="387">What are the steps to</text>
      <text x="80" y="411">selling a home?</text>
      <circle cx="56" cy="428" r="6" fill="var(--turquoise)"/>
      <text x="80" y="435">How do I open escrow?</text>
    </g>

    <rect class="web-pill" x="45" y="468" width="293" height="34" rx="17" fill="#ffffff"/>
    <text class="headline" x="191" y="492" font-size="19" fill="var(--turquoise)" text-anchor="middle">BrightlaneSkillhouse.com</text>

    <polygon class="footer-band" points="0,543 770,592 770,597 0,597" fill="var(--turquoise)"/>
    <polygon class="footer-strip" points="600,580 770,550 770,597 600,597" fill="var(--charcoal)"/>
    <polygon points="0,548 770,597 0,597" fill="var(--turquoise)"/>
  </svg>
</section>

</body>
</html>
```